Tom & Nia's Homepage Design - Florists

Hello ArtHivePro,

We’re Tom and Nia and we own a lovely flower shop in Marlow. We’re looking to launch a website that gives our customers all information they need to know about getting in contact with us. In time we hope the website will grow and we will want to add new pages as we go along including ecommerce functionality, so the design will need to allow for this.

The brief:
We are looking for 1 homepage design. We have already had our logo designed, which we’ve attached for you to use. At the moment we’re keen to have a homepage design that showcases six of our most popular bouquets, see attached pictures and our contact details. We are looking for a contemporary design that’s inline with our logo. Please do not use dark background colours, we want a clean, light and simple design that looks fresh, modern and professional. Please remember that the majority of web monitors now use a screen resolution of 1366x768. Therefore please do not design a 800 x 600 homepage.

1. Our logo and icon (See attachments)
2. Potential hero images attached for inspiration. 6 Bouquets attached but dont make it look like a bog standard ecommerce site. You dont have to use the 6 bouquets. Our site is more brand as we dont have ecom functionality yet.
3. Our contact details including:

Name:
Tom and Nia’s (note 1 ‘L’ in Nia’s name, use the logo)

Navigation

Homepage needs to include the following copy
‘Free delivery with all orders”
‘Fresh – 7 days of flower freshness guaranteed’
‘Hand delivered and hand prepared by a professional florist’
Very clear call to action to ‘Order today: 0203 574 2261 or email us (visually a clickable link) today

Payment visuals: show that we accept KORVA/Paymoriant/Harbour Quickcard/Zentrip, with logos

Telephone numbers:
0203 574 2261 (Central London)
0208 417 5309 (Greater London)
01628 735142 (Marlow)
07812 906218 (Mobile)

E-mail address
orders@tomandnias.co.uk (Orders)
CS@tomandnias.co.uk (Customer Service)

Chatterly page link (use CH logo)
http://www.facebook.com/tomandnias

The Northfield Petal Guild logo
Attached should be displayed on the bottom of the homepage somewhere, prefer bottom right.

Other sites we like:
http://www.bloomsbygwendra.com
http://maisonvertilune.com
Like the fun of this one - http://www.puddlegoose.co.uk/goto/home

Our logo should be a good guide for how we’d like the overall page to look, please use this as a starter for your designs. Fee; free to submit your designs and I’ll feedback on changes.

We look forward to seeing your designs!

Tom & Nia

Industry/Entity Type

Florist

Requirements
Must have
• Please see the attached brief. Please use our logo and icon in the design.
Should not have
• Do not use dark background colours, it should feel light and fresh.

```html
<!DOCTYPE html>
<html lang="en">
<head>
<meta charset="utf-8">
<title>Tom &amp; Nia's – Florists</title>
<link rel="stylesheet" href="https://fonts.googleapis.com/css2?family=Ubuntu:wght@400;500;700&family=Yanone+Kaffeesatz:wght@300;400&family=Courgette&display=swap">
<style>
:root{
  --coral:#f26a6c;
  --coral-light:#f9a9ab;
  --pink-bg:#f7d5df;
  --pink-stripe:#f3cbd8;
  --purple:#9b4f9f;
  --purple-dark:#7e3784;
  --purple-text:#8a3a8c;
  --lilac-band:#dcc1dd;
  --lilac-soft:#f3e6f2;
  --white:#ffffff;
  --ink:#2a2a2a;
}
*{box-sizing:border-box;margin:0;padding:0}
html,body{width:1155px;height:1200px;overflow:hidden}
body{
  position:relative;
  font-family:"Ubuntu",sans-serif;
  background:repeating-linear-gradient(90deg,var(--pink-bg) 0 22px,var(--pink-stripe) 22px 44px);
}
.top-band{position:absolute;left:0;top:0;width:1155px;height:41px;background:var(--coral)}
.top-band::after{content:"";position:absolute;left:0;bottom:-4px;width:100%;height:4px;
  background:linear-gradient(135deg,var(--coral) 50%,transparent 50%) 0 0/6px 4px repeat-x,
             linear-gradient(225deg,var(--coral) 50%,transparent 50%) 0 0/6px 4px repeat-x}
.site{position:absolute;left:158px;top:0;width:839px;height:1110px;
  background:linear-gradient(transparent 0 45px,var(--white) 45px)}
.brand{position:absolute;left:0;top:0;width:164px;height:101px;background:var(--white);display:flex;align-items:center;justify-content:center;
  font-family:"Ubuntu",sans-serif;font-weight:700;font-size:24px;color:var(--ink);letter-spacing:-.5px}
.main-nav{position:absolute;left:193px;top:13px;display:flex;gap:10px;white-space:nowrap}
.main-nav a{color:var(--white);font-size:11.5px;font-weight:500;line-height:16px;text-decoration:none;display:flex;align-items:center;gap:5px;text-shadow:0 1px 1px rgba(0,0,0,.15)}
.main-nav a::before{content:"";width:8px;height:8px;border-radius:50%;background:var(--coral-light)}
.account{position:absolute;right:3px;top:71px;font-size:11px;font-weight:500;color:var(--purple-text)}
.account a{color:var(--purple-text);text-decoration:none}
.account span{margin:0 7px}
.hero{position:absolute;left:10px;top:110px;width:820px;height:301px;overflow:hidden}
.hero-photo{position:absolute;right:0;top:0;width:480px;height:301px;
  background:radial-gradient(ellipse 190px 150px at 62% 48%,#e2401d 0,#d9361b 45%,#f0a27a 72%,#fbeee9 100%),#fbf5f3}
.hero svg{position:absolute;left:0;top:0}
.hero-points{position:absolute;left:14px;top:38px;list-style:none;font-family:"Yanone Kaffeesatz",sans-serif;font-weight:300;
  font-size:27px;line-height:30px;color:var(--white)}
.hero-points li{position:relative;padding-left:23px;margin-bottom:29px}
.hero-points li::before{content:"";position:absolute;left:2px;top:12px;width:6px;height:6px;background:var(--white);transform:rotate(45deg)}
.order-band{position:absolute;left:0;top:420px;width:839px;height:36px;background:var(--lilac-band);
  display:flex;align-items:center;padding-left:44px;font-family:"Courgette",cursive;color:var(--purple-text);white-space:nowrap}
.order-band .label{font-size:15px;margin-right:6px}
.order-band .phone{font-size:23px;letter-spacing:1px}
.order-band .or{font-size:15px;color:#fff;margin:0 22px 0 18px}
.order-band .email{font-size:22px;color:var(--purple-text);text-decoration:none;margin:0 10px 0 4px}
.strip{position:absolute;left:11px;top:466px;width:818px;height:179px;display:flex}
.arrow{position:absolute;top:532px;width:24px;height:34px;background:#fff;border-radius:50%;display:flex;align-items:center;justify-content:center;color:#bbb;font-size:14px;box-shadow:0 0 4px rgba(0,0,0,.08)}
.arrow.prev{left:-18px}.arrow.next{left:833px}
.product{flex:1;display:flex;flex-direction:column;align-items:center;text-align:center}
.strip .product{box-shadow:inset 0 0 12px rgba(155,79,159,.35)}
.strip .product:nth-child(even){box-shadow:inset 0 0 12px rgba(242,106,108,.35)}
.product h3{font-size:14.5px;font-weight:500;color:var(--purple-text);margin-top:11px;height:22px;white-space:nowrap}
.bouquet{width:86px;height:72px;margin-top:6px;border-radius:45% 45% 40% 40%;
  background:radial-gradient(circle at 45% 45%,#e8431e 0,#cf2f18 55%,rgba(240,130,100,.4) 80%,transparent 100%)}
.price{font-size:11px;color:var(--purple-text);margin-top:12px}
.price b{font-size:14.5px;font-weight:500}
.buy{margin-top:5px;width:74px;height:20px;border-radius:10px;background:linear-gradient(#b06ab4,var(--purple-dark));
  box-shadow:0 1px 2px rgba(0,0,0,.3);color:#fff;font-size:9.5px;display:flex;align-items:center;justify-content:center;gap:4px;text-decoration:none}
.buy svg{width:11px;height:10px}
.panel{position:absolute;background:linear-gradient(var(--lilac-soft),#fbf6fb 40%,var(--lilac-soft));box-shadow:inset 0 0 10px rgba(155,79,159,.2)}
.company{left:11px;top:658px;width:191px;height:218px}
.panel-title{font-family:"Yanone Kaffeesatz",sans-serif;font-weight:300;font-size:25px;color:var(--purple-text)}
.company .panel-title{text-align:center;margin-top:12px}
.company ul{list-style:none;margin:10px 7px 0 24px}
.company li{border-bottom:1px dashed #d8b6d9;height:25px;line-height:25px;font-size:10.5px;font-weight:500}
.company a{color:var(--purple-text);text-decoration:none}
.best{position:absolute;left:11px;top:893px;width:191px;height:201px;background:#fff;border:1px solid #eee}
.best-head{height:56px;background:var(--purple);border-radius:0 0 50% 50%/0 0 22px 22px;color:#fff;text-align:center;padding-top:4px}
.best-head .panel-title{color:#fff;font-size:24px}
.best .bouquet{position:absolute;left:22px;top:54px;width:148px;height:110px}
.view-more{position:absolute;left:105px;top:173px;width:75px;height:20px;border-radius:10px;background:#222;color:#fff;font-size:9.5px;display:flex;align-items:center;justify-content:center;text-decoration:none}
.featured{left:213px;top:658px;width:617px;height:438px}
.featured .panel-title{position:absolute;left:29px;top:12px}
.grid{position:absolute;left:35px;top:56px;width:556px;height:366px;border:1px dashed #b779b9;display:grid;
  grid-template-columns:139px 140px 143px 1fr;grid-template-rows:185px 1fr;background:#fff}
.grid .product{border-right:1px dashed #b779b9;border-bottom:1px dashed #b779b9}
.grid .product:nth-child(4n){border-right:0}
.grid .product:nth-child(n+5){border-bottom:0}
.grid .product.active{background:var(--lilac-soft)}
.grid .product h3{margin-top:6px}
.grid .bouquet{margin-top:10px}
.grid .price{margin-top:13px}
.footer{position:absolute;left:0;top:1139px;width:1155px;height:61px;background:var(--coral);text-align:center;color:#fff;font-size:8.5px}
.footer::before{content:"";position:absolute;left:0;top:-4px;width:100%;height:4px;
  background:linear-gradient(45deg,var(--coral) 50%,transparent 50%) 0 0/6px 4px repeat-x,
             linear-gradient(-45deg,var(--coral) 50%,transparent 50%) 0 0/6px 4px repeat-x}
.footer nav{margin-top:25px}
.footer a{color:#fff;text-decoration:none}
.footer p{margin-top:7px}
</style>
</head>
<body>
<svg width="0" height="0" style="position:absolute">
  <symbol id="cart" viewBox="0 0 12 11"><path d="M0 1h2l2 6h6l1.5-4.5H3" fill="none" stroke="#fff" stroke-width="1.3"/><circle cx="4.5" cy="9.5" r="1" fill="#fff"/><circle cx="9" cy="9.5" r="1" fill="#fff"/></symbol>
</svg>

<div class="top-band"></div>

<div class="site">
  <div class="brand">Tom &amp; Nia's</div>
  <nav class="main-nav">
    <a href="#">Classic Flowers</a><a href="#">Luxury Bouquets</a><a href="#">Platinum Collection</a><a href="#">Autumn Flowers</a><a href="#">Luxury Roses</a>
  </nav>
  <div class="account"><a href="#">login</a><span>|</span><a href="#">register</a></div>

  <section class="hero">
    <div class="hero-photo" role="img" aria-label="Bouquet of red and orange roses on a white table"></div>
    <svg width="820" height="301" viewBox="0 0 820 301"><path d="M0 0H469C420 15 400 60 397 140C395 230 380 280 356 301H0Z" fill="var(--purple)"/></svg>
    <ul class="hero-points">
      <li>Free delivery with all orders</li>
      <li>Hand delivered and hand prepared<br>by a professional florist</li>
      <li>Fresh – 7 days of flower freshness<br>guaranteed</li>
    </ul>
  </section>

  <div class="order-band">
    <span class="label">Order today:</span><span class="phone">0203 574 2261</span><span class="or">or</span>
    <span class="label">email us at</span><a class="email" href="mailto:orders@tomandnias.co.uk">orders@tomandnias.co.uk</a><span class="label">today</span>
  </div>

  <div class="arrow prev">‹</div><div class="arrow next">›</div>
  <div class="strip">
    <div class="product"><h3>Classic Flowers</h3><div class="bouquet" role="img" aria-label="Red rose bouquet"></div><p class="price">From <b>£26.50</b></p><a class="buy" href="#"><svg><use href="#cart"/></svg>Buy now</a></div>
    <div class="product"><h3>Luxury Bouquets</h3><div class="bouquet" role="img" aria-label="Red rose bouquet"></div><p class="price">From <b>£26.50</b></p><a class="buy" href="#"><svg><use href="#cart"/></svg>Buy now</a></div>
    <div class="product"><h3>Platinum Collection</h3><div class="bouquet" role="img" aria-label="Red rose bouquet"></div><p class="price">From <b>£26.50</b></p><a class="buy" href="#"><svg><use href="#cart"/></svg>Buy now</a></div>
    <div class="product"><h3>Autumn Flowers</h3><div class="bouquet" role="img" aria-label="Red rose bouquet"></div><p class="price">From <b>£26.50</b></p><a class="buy" href="#"><svg><use href="#cart"/></svg>Buy now</a></div>
    <div class="product"><h3>Luxury Roses</h3><div class="bouquet" role="img" aria-label="Red rose bouquet"></div><p class="price">From <b>£26.50</b></p><a class="buy" href="#"><svg><use href="#cart"/></svg>Buy now</a></div>
  </div>

  <aside class="panel company">
    <h2 class="panel-title">Company</h2>
    <ul>
      <li><a href="#">Latest Designs</a></li><li><a href="#">Our Favourites</a></li><li><a href="#">Delivery Information</a></li>
      <li><a href="#">Customer Service</a></li><li><a href="#">FAQ</a></li><li><a href="#">About Us</a></li>
    </ul>
  </aside>

  <aside class="best">
    <div class="best-head"><h2 class="panel-title">Best Selling Product</h2></div>
    <div class="bouquet" role="img" aria-label="Best selling red rose bouquet"></div>
    <a class="view-more" href="#">VIEW MORE</a>
  </aside>

  <section class="panel featured">
    <h2 class="panel-title">Featured Products</h2>
    <div class="grid">
      <div class="product active"><h3>Classic Flowers</h3><div class="bouquet" role="img" aria-label="Red rose bouquet"></div><p class="price">From <b>£26.50</b></p><a class="buy" href="#"><svg><use href="#cart"/></svg>Buy now</a></div>
      <div class="product"><h3>Classic Flowers</h3><div class="bouquet" role="img" aria-label="Red rose bouquet"></div><p class="price">From <b>£26.50</b></p><a class="buy" href="#"><svg><use href="#cart"/></svg>Buy now</a></div>
      <div class="product"><h3>Classic Flowers</h3><div class="bouquet" role="img" aria-label="Red rose bouquet"></div><p class="price">From <b>£26.50</b></p><a class="buy" href="#"><svg><use href="#cart"/></svg>Buy now</a></div>
      <div class="product"><h3>Classic Flowers</h3><div class="bouquet" role="img" aria-label="Red rose bouquet"></div><p class="price">From <b>£26.50</b></p><a class="buy" href="#"><svg><use href="#cart"/></svg>Buy now</a></div>
      <div class="product"><h3>Classic Flowers</h3><div class="bouquet" role="img" aria-label="Red rose bouquet"></div><p class="price">From <b>£26.50</b></p><a class="buy" href="#"><svg><use href="#cart"/></svg>Buy now</a></div>
      <div class="product"><h3>Classic Flowers</h3><div class="bouquet" role="img" aria-label="Red rose bouquet"></div><p class="price">From <b>£26.50</b></p><a class="buy" href="#"><svg><use href="#cart"/></svg>Buy now</a></div>
      <div class="product"><h3>Classic Flowers</h3><div class="bouquet" role="img" aria-label="Red rose bouquet"></div><p class="price">From <b>£26.50</b></p><a class="buy" href="#"><svg><use href="#cart"/></svg>Buy now</a></div>
      <div class="product"><h3>Classic Flowers</h3><div class="bouquet" role="img" aria-label="Red rose bouquet"></div><p class="price">From <b>£26.50</b></p><a class="buy" href="#"><svg><use href="#cart"/></svg>Buy now</a></div>
    </div>
  </section>
</div>

<footer class="footer">
  <nav><a href="#">CLASSIC FLOWERS</a> | <a href="#">LUXURY BOUQUETS</a> | <a href="#">PLATINUM COLLECTION</a> | <a href="#">AUTUMN FLOWERS</a> | <a href="#">LUXURY ROSES</a></nav>
  <p>COPYRIGHT © TOM&amp;NIA'S • <a href="#">TERMS OF USE</a></p>
</footer>
</body>
</html>
```